DENTIST OFFICE POST CARD DESIGN

COMPANY NAME: BEARABLE DENTISTRYCome and see if Meridale Dentistry is for you.... ALWAYSWELCOMINGNEW PATIENTS!Call today for your appointment!607 918 2763 We are located on 14 Palvin Street , Oneonta, Ny----(map scketch)All in one stop for all your dental care needsCOSMETIC DENTISTRYDENTAL IMPLANTSROOT CANALSVENEERSWHITENINGSFILLINGSCROWNSBRIDGESDENTURESEXTRACTIONSGUM TREATMENTSSNAP ON SMILECOLOR------ANYPOSTCARD INDICIA;PRSRT STDECRWSSU.S. POSTAGEPAIDEDDM RETAILLocalPostal Customer

```html
<!DOCTYPE html>
<html lang="en">
<head>
<meta charset="utf-8">
<title>Meridale Dentistry – Postcard</title>
<link href="https://fonts.googleapis.com/css2?family=Kreon:wght@300;400&family=Source+Sans+3:wght@400;600;700&family=Roboto+Condensed:wght@400;700&family=Arimo:wght@400;700&display=swap" rel="stylesheet">
<style>
  :root {
    --purple: #55308f;
    --green: #8cc63f;
    --sky: #eef6fa;
    --ring: #a59ad1;
    --white: #ffffff;
    --ink: #1e1e1e;
    --grey: #5a5a5a;
    --page: #e7e7ea;
  }
  * { box-sizing: border-box; margin: 0; padding: 0; }
  html, body { width: 1200px; height: 1151px; overflow: hidden; }
  body { background: var(--page); position: relative; font-family: "Source Sans 3", sans-serif; }

  .card { position: absolute; background: var(--white); overflow: hidden; box-shadow: 0 4px 14px rgba(0,0,0,.18); }
  .card--front { left: 97px; top: 85px; width: 859px; height: 472px; }
  .card--back { left: 182px; top: 608px; width: 857px; height: 471px; }
  .card__shapes { position: absolute; inset: 0; width: 100%; height: 100%; }
  .abs { position: absolute; }

  .brand-title { font-family: "Kreon", serif; font-weight: 300; color: var(--white); line-height: 1; white-space: nowrap; }
  .brand-title--front { left: 471px; top: 14px; font-size: 43px; }
  .brand-title--back { left: 31px; top: 12px; font-size: 37px; }
  .brand-address { left: 469px; top: 64px; font-family: "Kreon", serif; font-weight: 400; color: var(--white); font-size: 17px; letter-spacing: 1.5px; white-space: nowrap; }
  .tagline { left: 31px; top: 62px; font-family: "Kreon", serif; font-weight: 400; color: var(--white); font-size: 14.5px; white-space: nowrap; }

  .front-teaser { left: 41px; top: 26px; color: var(--purple); font-size: 28px; line-height: 31.5px; }

  .badge { position: absolute; border-radius: 50%; background: var(--white); border: 5px solid var(--ring);
    display: flex; align-items: center; justify-content: center; text-align: center;
    font-family: "Roboto Condensed", sans-serif; font-weight: 700; color: var(--purple); font-size: 17.5px; line-height: 22px; }

  .cta { position: absolute; color: var(--white); text-align: center; }
  .cta__lead { font-weight: 600; font-size: 22px; white-space: nowrap; }
  .cta__phone { display: flex; align-items: center; justify-content: center; gap: 12px; font-weight: 700; font-size: 31px; margin-top: 0; }
  .phone-icon { width: 32px; height: 26px; }

  .back-cta .cta__lead { font-family: "Roboto Condensed", sans-serif; font-weight: 400; font-size: 19.5px; }
  .back-cta .cta__phone { font-family: "Roboto Condensed", sans-serif; font-size: 27px; margin-top: 10px; }

  .mailer-address { left: 493px; top: 16px; color: var(--ink); font-size: 18.5px; line-height: 19.5px; font-style: normal; }
  .mailer-address__name { color: var(--purple); font-size: 18.5px; margin-bottom: 16px; }

  .indicia { left: 776px; top: 70px; width: 62px; height: 62px; border: 1px solid #222; font-family: "Arimo", sans-serif;
    font-weight: 700; font-size: 7.5px; line-height: 9.6px; text-align: center; color: #111; padding-top: 6px; }
  .recipient { left: 594px; top: 164px; width: 243px; height: 77px; border: 1px solid #222; font-family: "Arimo", sans-serif;
    font-size: 13.5px; line-height: 16px; color: #111; padding: 20px 0 0 24px; }

  .services-intro { left: 33px; top: 140px; color: var(--purple); font-size: 21px; white-space: nowrap; }
  .services { position: absolute; top: 168px; list-style: none; color: var(--purple); font-size: 22px; line-height: 24.7px; }
  .services--a { left: 33px; }
  .services--b { left: 263px; }
  .services li { display: flex; align-items: center; gap: 3px; white-space: nowrap; }
  .bullet { width: 15px; height: 15px; flex: none; }

  .location-note { left: 30px; top: 331px; font-size: 11px; color: var(--grey); white-space: nowrap; }
  .map-area { left: 30px; top: 348px; width: 353px; height: 114px;
    background: linear-gradient(135deg, #eceae4 0%, #e3e6dc 45%, #d9e6c8 70%, #ecebe6 100%); }
</style>
</head>
<body>

<section class="card card--front">
  <svg class="card__shapes" viewBox="0 0 859 472" preserveAspectRatio="none" aria-hidden="true">
    <defs>
      <linearGradient id="familyTone" x1="0" y1="0" x2="1" y2="0">
        <stop offset="0" stop-color="#c9d6b6"/>
        <stop offset=".35" stop-color="#e5c2a6"/>
        <stop offset=".7" stop-color="#f0dccb"/>
        <stop offset="1" stop-color="#f6f6f6"/>
      </linearGradient>
      <linearGradient id="mouthTone" x1="0" y1="0" x2="1" y2="1">
        <stop offset="0" stop-color="#f5e3dc"/>
        <stop offset=".5" stop-color="#e7a9a8"/>
        <stop offset="1" stop-color="#f1d2c6"/>
      </linearGradient>
    </defs>
    <g role="img" aria-label="Photo of a smiling family of four">
      <rect x="0" y="90" width="859" height="291" fill="url(#familyTone)"/>
    </g>
    <path d="M0,0 H470 C380,80 200,125 0,132 Z" fill="var(--sky)"/>
    <path d="M0,130 C190,124 360,72 462,0 H482 C400,78 230,150 0,163 Z" fill="var(--green)"/>
    <path d="M478,0 H859 V103 H250 C340,84 420,44 478,0 Z" fill="var(--purple)"/>
    <rect x="0" y="381" width="620" height="6" fill="var(--white)"/>
    <rect x="0" y="387" width="620" height="85" fill="var(--purple)"/>
    <g role="img" aria-label="Close-up photo of a smile with a dental mirror">
      <path d="M859,232 C720,262 600,350 512,472 H859 Z" fill="url(#mouthTone)"/>
    </g>
    <path d="M859,203 V234 C720,262 600,350 512,472 H490 C570,335 700,228 859,203 Z" fill="var(--green)"/>
  </svg>

  <p class="abs front-teaser">Come and see if<br>Meridale Dentistry<br>is for you...</p>
  <h1 class="abs brand-title brand-title--front">Meridale Dentistry</h1>
  <p class="abs brand-address">14 Palvin Street. Oneonta, Ny, 13820</p>

  <div class="cta" style="left:22px; top:394px; width:400px;">
    <p class="cta__lead">Call today for your appointment!</p>
    <p class="cta__phone">
      <svg class="phone-icon" viewBox="0 0 32 26" aria-hidden="true"><rect width="32" height="26" rx="2" fill="var(--white)"/><path transform="translate(4,1)" d="M6.6 10.8c1.4 2.8 3.8 5.1 6.6 6.6l2.2-2.2c.3-.3.7-.4 1-.2 1.1.4 2.3.6 3.6.6.6 0 1 .4 1 1V20c0 .6-.4 1-1 1C10.6 21 3 13.4 3 4c0-.6.4-1 1-1h3.5c.6 0 1 .4 1 1 0 1.3.2 2.5.6 3.6.1.3 0 .7-.2 1L6.6 10.8z" fill="var(--purple)"/></svg>
      607 918 2763
    </p>
  </div>

  <div class="badge" style="left:475px; top:311px; width:136px; height:136px;">ALWAYS<br>WELCOMING<br>NEW PATIENTS!</div>
</section>

<section class="card card--back">
  <svg class="card__shapes" viewBox="0 0 857 471" preserveAspectRatio="none" aria-hidden="true">
    <path d="M0,0 H458 C380,78 250,104 0,108 Z" fill="var(--purple)"/>
    <path d="M0,108 C250,104 380,78 458,0 H472 C400,92 250,122 0,125 Z" fill="var(--green)"/>
    <path d="M857,342 V471 H410 C500,400 650,355 857,342 Z" fill="var(--purple)"/>
    <path d="M857,312 V342 C650,355 500,400 410,471 H390 C480,378 650,322 857,312 Z" fill="var(--green)"/>
  </svg>

  <h2 class="abs brand-title brand-title--back">Meridale Dentistry</h2>
  <p class="abs tagline">We'll Provide You With That Winning Smile!</p>

  <address class="abs mailer-address">
    <p class="mailer-address__name">MERIDALE DENTISTRY</p>
    <p>14 Palvin Street</p>
    <p>Oneonta, NY 13820</p>
    <p>607-918-2763</p>
    <p>www.meridaledentist.com</p>
  </address>

  <div class="abs indicia">PRSRT STD<br>ECRWSS<br>U.S. POSTAGE<br>PAID<br>EDDM RETAIL</div>
  <div class="abs recipient">Local<br>Postal Customer</div>

  <p class="abs services-intro">All in one stop for all your dental care needs</p>
  <svg width="0" height="0" style="position:absolute" aria-hidden="true">
    <symbol id="bullet" viewBox="0 0 16 16"><circle cx="8" cy="8" r="8" fill="var(--purple)"/><path d="M6.3 4.3 L10 8 L6.3 11.7" fill="none" stroke="var(--white)" stroke-width="2.2"/></symbol>
  </svg>
  <ul class="services services--a">
    <li><svg class="bullet"><use href="#bullet"/></svg>Cosmetic Dentistry</li>
    <li><svg class="bullet"><use href="#bullet"/></svg>Dental Implants</li>
    <li><svg class="bullet"><use href="#bullet"/></svg>Root Canals</li>
    <li><svg class="bullet"><use href="#bullet"/></svg>Veneers</li>
    <li><svg class="bullet"><use href="#bullet"/></svg>Whitening</li>
    <li><svg class="bullet"><use href="#bullet"/></svg>Fillings</li>
  </ul>
  <ul class="services services--b">
    <li><svg class="bullet"><use href="#bullet"/></svg>Crowns</li>
    <li><svg class="bullet"><use href="#bullet"/></svg>Bridges</li>
    <li><svg class="bullet"><use href="#bullet"/></svg>Denture</li>
    <li><svg class="bullet"><use href="#bullet"/></svg>Extraction</li>
    <li><svg class="bullet"><use href="#bullet"/></svg>Gum Treatments</li>
    <li><svg class="bullet"><use href="#bullet"/></svg>Clip Fit Grin</li>
  </ul>

  <p class="abs location-note">We are located on 14 Palvin Street, Oneonta, Ny</p>
  <div class="abs map-area" role="img" aria-label="Street map showing the office location"></div>

  <div class="badge" style="left:400px; top:309px; width:130px; height:130px;">ALWAYS<br>WELCOMING<br>NEW PATIENTS!</div>

  <div class="cta back-cta" style="left:580px; top:384px; width:260px;">
    <p class="cta__lead">Call today for your appointment!</p>
    <p class="cta__phone">
      <svg class="phone-icon" viewBox="0 0 32 26" style="width:26px;height:22px" aria-hidden="true"><rect width="32" height="26" rx="2" fill="var(--white)"/><path transform="translate(4,1)" d="M6.6 10.8c1.4 2.8 3.8 5.1 6.6 6.6l2.2-2.2c.3-.3.7-.4 1-.2 1.1.4 2.3.6 3.6.6.6 0 1 .4 1 1V20c0 .6-.4 1-1 1C10.6 21 3 13.4 3 4c0-.6.4-1 1-1h3.5c.6 0 1 .4 1 1 0 1.3.2 2.5.6 3.6.1.3 0 .7-.2 1L6.6 10.8z" fill="var(--purple)"/></svg>
      607 918 2763
    </p>
  </div>
</section>

</body>
</html>
```